Geothermal company needs a creative "POW" business card

Manufacturers tend to be boring. We are not! We are a Geothermal Heat Pump company that has over 30 yrs of experience and wants a new look and updated feel. Nothing old (yawn) so get your creative hats on and let's rock!

We want to use the great colors of lime green and navy blue. Our new logo is attached and we're ready to roll. Remember, we're a professional leader in the geothermal industry that needs to make an eye catching and memorable first glance.

```html
<!DOCTYPE html>
<html lang="en">
<head>
<meta charset="utf-8">
<title>Boreal Thermal Business Card</title>
<link rel="stylesheet" href="https://fonts.googleapis.com/css2?family=Ubuntu:wght@500;700&family=Open+Sans:wght@700;800&family=Arimo:wght@400&display=swap">
<style>
  :root {
    --lime: #8cc63f;
    --lime-light: #b5dc6e;
    --navy: #1b2f6b;
    --white: #ffffff;
    --ink: #1a1a1a;
    --title-yellow: #e6e619;
    --backdrop: #e9ebe6;
  }
  * { margin: 0; padding: 0; box-sizing: border-box; }
  html, body {
    width: 1200px; height: 1200px; overflow: hidden;
    background: var(--backdrop);
  }
  .sheet {
    position: relative; width: 1200px; height: 1200px;
    display: flex; flex-direction: column; align-items: center; justify-content: center; gap: 40px;
  }
  .card {
    position: relative; width: 900px; height: 514px;
    background: var(--white); overflow: hidden;
    box-shadow: 0 10px 30px rgba(0,0,0,0.18);
  }
  .card-waves { position: absolute; inset: 0; width: 100%; height: 100%; }
  .wave { fill: var(--lime); }
  .wave-highlight { fill: var(--lime-light); }
  .wave-gap { fill: var(--white); }

  /* Front */
  .brand {
    position: absolute; left: 130px; top: 150px;
    display: flex; align-items: center; gap: 34px;
  }
  .brand-dot { width: 120px; height: 120px; border-radius: 50%; background: var(--navy); flex: none; }
  .brand-name {
    font-family: "Ubuntu", sans-serif; font-weight: 700;
    font-size: 64px; line-height: 1; color: var(--lime); letter-spacing: 0.5px;
  }
  .brand-tagline {
    margin-top: 8px;
    font-family: "Ubuntu", sans-serif; font-weight: 500;
    font-size: 19px; color: var(--navy);
  }

  /* Back */
  .holder { position: absolute; left: 130px; top: 48px; font-family: "Open Sans", sans-serif; font-weight: 800; }
  .holder-name { font-size: 30px; color: var(--white); letter-spacing: 0.5px; }
  .holder-title { font-size: 20px; color: var(--title-yellow); margin-left: 95px; margin-top: -2px; }

  .back-mark {
    position: absolute; left: 95px; top: 185px; width: 260px;
    display: flex; flex-direction: column; align-items: center; gap: 18px;
  }
  .back-mark .brand-dot { width: 170px; height: 170px; }
  .back-mark .brand-name { font-size: 30px; }

  .contacts {
    position: absolute; left: 420px; top: 150px; list-style: none;
    font-family: "Arimo", sans-serif; font-size: 17px; color: var(--ink);
  }
  .contacts li { display: flex; align-items: center; gap: 14px; height: 30px; margin-bottom: 4px; }
  .contact-icon { width: 24px; height: 24px; flex: none; }
  .contact-icon rect { fill: var(--lime); }
  .contact-icon .glyph { fill: none; stroke: var(--white); stroke-width: 1.6; stroke-linecap: round; stroke-linejoin: round; }

  .back-tagline {
    position: absolute; left: 0; right: 0; bottom: 34px; text-align: center;
    font-family: "Open Sans", sans-serif; font-weight: 700;
    font-size: 21px; color: var(--white); letter-spacing: 0.4px;
  }
</style>
</head>
<body>
<main class="sheet">

  <section class="card card-front">
    <svg class="card-waves" viewBox="0 0 900 514" preserveAspectRatio="none" aria-hidden="true">
      <path class="wave" d="M470,0 C640,8 800,45 900,120 L900,0 Z"/>
      <path class="wave-gap" d="M760,0 C820,10 870,30 900,55 L900,40 C870,20 830,5 790,0 Z"/>
      <path class="wave" d="M0,514 L0,390 C220,320 470,420 680,335 C790,290 860,255 900,240 L900,514 Z"/>
      <path class="wave-highlight" d="M680,335 C790,290 860,255 900,240 L900,300 C850,320 780,345 700,352 Z" opacity="0.55"/>
      <path class="wave-gap" d="M820,514 C860,430 880,360 900,300 L900,330 C885,390 870,450 850,514 Z"/>
    </svg>
    <div class="brand">
      <span class="brand-dot"></span>
      <div>
        <div class="brand-name">Boreal Thermal</div>
        <div class="brand-tagline">Manufacturer of Geothermal Heat Pumps for the North</div>
      </div>
    </div>
  </section>

  <section class="card card-back">
    <svg class="card-waves" viewBox="0 0 900 514" preserveAspectRatio="none" aria-hidden="true">
      <path class="wave" d="M0,0 L900,0 L900,22 C720,30 520,150 280,140 C170,136 70,118 0,122 Z"/>
      <path class="wave-gap" d="M760,0 C820,8 870,25 900,45 L900,30 C870,14 830,4 800,0 Z"/>
      <path class="wave" d="M0,514 L0,415 C210,470 460,425 660,370 C790,335 860,300 900,280 L900,514 Z"/>
      <path class="wave-gap" d="M830,514 C865,430 885,360 900,320 L900,350 C888,400 875,460 860,514 Z"/>
    </svg>

    <div class="holder">
      <div class="holder-name">RAY LINDQVIST</div>
      <div class="holder-title">CEO</div>
    </div>

    <div class="back-mark">
      <span class="brand-dot"></span>
      <div class="brand-name">Boreal Thermal</div>
    </div>

    <ul class="contacts">
      <li>
        <svg class="contact-icon" viewBox="0 0 24 24" aria-hidden="true"><rect width="24" height="24" rx="3"/><path class="glyph" d="M12 19 C8 14 7 12 7 10 a5 5 0 0 1 10 0 c0 2 -1 4 -5 9 Z"/><circle class="glyph" cx="12" cy="10" r="1.8"/></svg>
        <span>42 N Birch St, Fairhaven, MN 56100</span>
      </li>
      <li>
        <svg class="contact-icon" viewBox="0 0 24 24" aria-hidden="true"><rect width="24" height="24" rx="3"/><path class="glyph" d="M8 5 L10 9 L8.5 10.5 C9.5 12.5 11.5 14.5 13.5 15.5 L15 14 L19 16 L17.5 19 C11 18.5 5.5 13 5 6.5 Z"/></svg>
        <span>(320) 555-0142</span>
      </li>
      <li>
        <svg class="contact-icon" viewBox="0 0 24 24" aria-hidden="true"><rect width="24" height="24" rx="3"/><rect class="glyph" x="6" y="10" width="12" height="7" style="fill:none"/><path class="glyph" d="M8 10 V5 H16 V10 M9 14 H15"/></svg>
        <span>(320) 555-0143</span>
      </li>
      <li>
        <svg class="contact-icon" viewBox="0 0 24 24" aria-hidden="true"><rect width="24" height="24" rx="3"/><path class="glyph" d="M5 7 H19 V17 H5 Z M5 7 L12 13 L19 7"/></svg>
        <span>raylindqvist@borealthermal.com</span>
      </li>
      <li>
        <svg class="contact-icon" viewBox="0 0 24 24" aria-hidden="true"><rect width="24" height="24" rx="3"/><circle class="glyph" cx="12" cy="12" r="6.5"/><path class="glyph" d="M5.5 12 H18.5 M12 5.5 C9 9 9 15 12 18.5 M12 5.5 C15 9 15 15 12 18.5"/></svg>
        <span>www.borealthermal.com</span>
      </li>
    </ul>

    <div class="back-tagline">MANUFACTURER OF GEOTHERMAL HEAT PUMPS FOR THE NORTH</div>
  </section>

</main>
</body>
</html>
```